Brindlow display card for Break Loose At Pier 4

we need to design a display card for an break loose at pier 4 gift card that will be selling in brindlow. I' attached the specs and our logo, our website is breaklooseatpier4.com.

the offer will be 2x $50.00 gift cards for $79.99.

i also prefer our logo with the black background.

```html
<!DOCTYPE html>
<html lang="en">
<head>
<meta charset="utf-8">
<title>Brindlow display card – Break Loose At Pier 4</title>
<link href="https://fonts.googleapis.com/css2?family=Anton&family=Montserrat:wght@300;400&family=Roboto+Condensed:wght@700&display=swap" rel="stylesheet">
<style>
  :root{
    --page:#2b2b2d;
    --card-top:#3a3b3e;
    --card-dark:#111214;
    --teal:#2f6c87;
    --teal-deep:#1b3f52;
    --white:#ffffff;
    --magenta:#e0197d;
  }
  *{box-sizing:border-box;margin:0;padding:0}
  html,body{width:1200px;height:900px;overflow:hidden;background:var(--page)}
  .canvas{position:relative;width:1200px;height:900px}

  .card{
    position:absolute;top:125px;width:503px;height:650px;
    border-radius:34px 34px 42px 42px;overflow:hidden;
    background:var(--card-dark);
    box-shadow:0 10px 26px rgba(0,0,0,.45);
  }
  .card--front{left:87px}
  .card--back{left:612px}

  .card__art{
    position:absolute;inset:0;
    background:
      linear-gradient(135deg, rgba(255,255,255,0) 52%, rgba(255,255,255,.07) 52%, rgba(255,255,255,.03) 100%),
      radial-gradient(circle at 50% 55%, var(--teal) 0%, var(--teal-deep) 45%, var(--card-dark) 85%);
  }
  .card--front .card__art{top:66px;bottom:38px}

  .hang-slot{
    position:absolute;top:22px;left:50%;transform:translateX(-50%);
    width:56px;height:20px;border-radius:10px;background:var(--page);
    box-shadow:inset 0 1px 3px rgba(0,0,0,.6);z-index:3
  }

  .header-strip{
    position:absolute;top:0;left:0;right:0;height:62px;
    background:var(--card-top);border-bottom:4px solid var(--white);z-index:2
  }
  .footer-strip{
    position:absolute;bottom:0;left:0;right:0;height:40px;
    background:var(--card-dark);border-top:4px solid var(--white);z-index:2
  }
  .notice{
    position:absolute;font-family:"Roboto Condensed",Arial,sans-serif;
    font-weight:700;font-size:8.4px;line-height:1.2;color:var(--white);
    text-transform:uppercase
  }
  .notice--en-top{left:28px;top:22px}
  .notice--fr-top{left:310px;top:22px}
  .notice--en-bottom{left:28px;top:8px}
  .notice--fr-bottom{left:285px;top:8px}

  .price{
    position:absolute;right:22px;top:84px;z-index:2;
    font-family:"Montserrat",sans-serif;font-weight:300;font-size:42px;
    color:var(--white);letter-spacing:1px
  }
  .brand{
    position:absolute;left:110px;top:180px;z-index:2;display:flex;align-items:flex-start;gap:14px
  }
  .brand__name{
    font-family:"Anton",Impact,sans-serif;font-weight:400;color:var(--white);
    font-size:82px;line-height:.98;text-transform:uppercase
  }
  .brand__dot{width:44px;height:44px;border-radius:50%;background:var(--teal);margin-top:238px}
  .product-label{
    position:absolute;left:0;right:0;top:518px;text-align:center;z-index:2;
    font-family:"Montserrat",sans-serif;font-weight:300;font-size:38px;
    letter-spacing:9px;color:var(--white);padding-left:8px
  }

  .item-tag{position:absolute;z-index:2;text-align:center}
  .card--front .item-tag{right:24px;top:575px}
  .card--back .item-tag{right:50px;top:585px}
  .item-tag__label{font-family:"Roboto Condensed",Arial,sans-serif;font-weight:700;font-size:7px;color:var(--white)}
  .item-tag__fpo{
    margin-top:2px;background:var(--magenta);color:var(--white);
    font-family:"Roboto Condensed",Arial,sans-serif;font-weight:700;font-size:13px;
    padding:2px 8px;border:2px solid var(--white)
  }
</style>
</head>
<body>
<main class="canvas">

  <section class="card card--front" aria-label="Gift card display, front">
    <div class="card__art" role="img" aria-label="Brand emblem artwork in deep teal on black"></div>
    <div class="hang-slot"></div>
    <header class="header-strip">
      <p class="notice notice--en-top">To purchase this item, please take this<br>card to the cash register and exchange<br>for the quantity you wish to purchase.</p>
      <p class="notice notice--fr-top">Veuillez présenter cette carte à la<br>caisse pour l'échanger contre le nombre<br>d'articles que vous souhaitez acheter.</p>
    </header>

    <p class="price">$50.00</p>
    <div class="brand">
      <h1 class="brand__name">Break<br>Loose At<br>Pier 4</h1>
      <span class="brand__dot"></span>
    </div>
    <p class="product-label">GIFT CARD</p>

    <div class="item-tag">
      <p class="item-tag__label">ITM./ART.</p>
      <p class="item-tag__fpo">F.P.O.</p>
    </div>

    <footer class="footer-strip">
      <p class="notice notice--en-bottom">Do not remove this card from the warehouse.<br>This card has no monetary value.</p>
      <p class="notice notice--fr-bottom">Ne pas sortir cette carte de l'entrepôt.<br>Cette carte n'a aucune valeur marchande.</p>
    </footer>
  </section>

  <section class="card card--back" aria-label="Gift card display, back">
    <div class="card__art" role="img" aria-label="Large brand emblem decoration in teal on black"></div>
    <div class="hang-slot"></div>
    <div class="item-tag">
      <p class="item-tag__label">ITM./ART.</p>
      <p class="item-tag__fpo">F.P.O.</p>
    </div>
  </section>

</main>
</body>
</html>
```